Every Drawer Neatly Sorted or EDN Organized needs a business card design. EDN Organized is a professi

We need a business card design that is clean, sharp and conveys a sense of organization. I already have a logo.

Target Market(s)

Families (specifically mothers), small business owners, parents, seniors

Industry/Entity Type

Business

Contact Information for Business Card

My website is www.ednorganized-example.com and my Facebook page is http://www.socialpage-example.com/everydrawerneatlysorted. The phone number is 555-418-2706 and I want to be listed as Miriel O. Dunsford, Owner

Requirements
Must have
• My logo.

```html
<!DOCTYPE html>
<html lang="en">
<head>
<meta charset="utf-8">
<title>EDN Organized — Business Card</title>
<link rel="stylesheet" href="https://fonts.googleapis.com/css2?family=Montserrat:wght@400;500&family=Lora:wght@400&display=swap">
<style>
  :root {
    --page-bg: #ecebe8;
    --card-bg: #ffffff;
    --brand-blue: #0b74b6;
    --ink: #231f20;
    --on-blue: #ffffff;
  }
  * { box-sizing: border-box; margin: 0; padding: 0; }
  html, body {
    width: 1200px;
    height: 1200px;
    overflow: hidden;
    background: var(--page-bg);
  }
  .canvas {
    width: 1200px;
    height: 1200px;
    display: flex;
    align-items: center;
    justify-content: center;
  }
  .card {
    position: relative;
    width: 1000px;
    height: 572px;
    background: var(--card-bg);
    box-shadow: 0 6px 18px rgba(0,0,0,0.18);
    font-family: "Montserrat", Arial, sans-serif;
    color: var(--ink);
  }
  .brand {
    position: absolute;
    top: 118px;
    left: 0;
    right: 0;
    display: flex;
    align-items: center;
    justify-content: center;
    gap: 22px;
  }
  .brand-mark {
    width: 30px;
    height: 30px;
    background: var(--brand-blue);
  }
  .brand-name {
    font-family: "Montserrat", Arial, sans-serif;
    font-weight: 400;
    font-size: 52px;
    letter-spacing: 6px;
    color: var(--ink);
  }
  .info-band {
    position: absolute;
    top: 252px;
    left: 0;
    width: 100%;
    height: 154px;
    background: var(--brand-blue);
    color: var(--on-blue);
  }
  .person {
    position: absolute;
    top: 26px;
    right: 78px;
    text-align: right;
  }
  .person-name {
    font-family: "Lora", Georgia, serif;
    font-size: 36px;
    font-weight: 400;
    line-height: 1.1;
  }
  .person-role {
    font-size: 22px;
    font-weight: 400;
    margin-top: 4px;
  }
  .contacts {
    position: absolute;
    left: 62px;
    bottom: 20px;
    list-style: none;
    font-size: 23px;
    line-height: 1.45;
  }
  .contacts li {
    display: flex;
    align-items: center;
    gap: 8px;
  }
  .contacts svg {
    width: 18px;
    height: 18px;
    flex: none;
  }
  .social {
    position: absolute;
    top: 448px;
    left: 0;
    right: 0;
    display: flex;
    align-items: center;
    justify-content: center;
    gap: 10px;
    font-size: 25px;
    color: var(--ink);
  }
  .social-square {
    width: 20px;
    height: 20px;
    background: var(--brand-blue);
  }
</style>
</head>
<body>
<main class="canvas">
  <article class="card">
    <header class="brand">
      <span class="brand-mark" aria-hidden="true"></span>
      <h1 class="brand-name">EDN Organized</h1>
    </header>

    <section class="info-band">
      <div class="person">
        <p class="person-name">Miriel O. Dunsford</p>
        <p class="person-role">Owner</p>
      </div>
      <ul class="contacts">
        <li>
          <svg viewBox="0 0 24 24" aria-hidden="true"><path fill="currentColor" d="M6.6 10.8a15.1 15.1 0 0 0 6.6 6.6l2.2-2.2a1 1 0 0 1 1-.25 11.4 11.4 0 0 0 3.6.57 1 1 0 0 1 1 1V20a1 1 0 0 1-1 1A17 17 0 0 1 3 4a1 1 0 0 1 1-1h3.5a1 1 0 0 1 1 1c0 1.25.2 2.46.57 3.6a1 1 0 0 1-.25 1z"/></svg>
          555-418-2706
        </li>
        <li>
          <svg viewBox="0 0 24 24" aria-hidden="true" fill="none" stroke="currentColor" stroke-width="1.6"><circle cx="12" cy="12" r="9.5"/><ellipse cx="12" cy="12" rx="4" ry="9.5"/><path d="M2.5 12h19M4 7h16M4 17h16"/></svg>
          www.ednorganized-example.com
        </li>
      </ul>
    </section>

    <p class="social">
      <span class="social-square" aria-hidden="true"></span>
      www.socialpage-example.com/everydrawerneatlysorted
    </p>
  </article>
</main>
</body>
</html>
```